Brackwell Immigration Law

We need a web design for our existing company www.brackwellcounsel.co.uk. We are an immigration consultancy. The final design should communicate professionalism, integrity and affordability.

Industry/Entity Type

It Company

Logo Text

Brackwell Counsel Partners

Number of Pages Required

5+ page

Font styles to use
Serif

Requirements
Must have
• I want to have the same silhouette logo but something different in positioning..
Nice to have
• Please have a look at these websites:
• https://www.travelpathguide.co.uk/visa_uk/
• http://www.oakdenadvisers.co.uk/
• http://www.myrtlegatelaw.org/index.php
• www.brackwellcounsel.co.uk

```html
<!DOCTYPE html>
<html lang="en">
<head>
<meta charset="utf-8">
<title>Brackwell Counsel Partners</title>
<link href="https://fonts.googleapis.com/css2?family=Noto+Serif:ital,wght@0,400;0,700;1,400&display=swap" rel="stylesheet">
<style>
:root{
  --ink:#2b2b2b;
  --muted:#555;
  --navy:#2f4a7d;
  --band:#3b3b3b;
  --band-dark:#2e2e2e;
  --rule:#d9d9d9;
  --social-a:#3b5998;
  --social-b:#1da1f2;
  --white:#fff;
}
*{box-sizing:border-box;margin:0;padding:0}
html,body{width:1200px;height:2352px;overflow:hidden;background:var(--white)}
body{font-family:"Noto Serif",Georgia,serif;color:var(--ink);position:relative}
.site-header{position:absolute;top:0;left:0;width:1200px;height:148px}
.brand{position:absolute;left:64px;top:44px;display:flex;align-items:center;gap:12px}
.brand-mark{width:40px;height:40px;border-radius:50%;background:var(--ink)}
.brand-name{font-size:17px;color:var(--ink);width:130px;line-height:1.2}
.main-nav{position:absolute;left:392px;top:68px;display:flex;gap:38px;font-size:16px}
.main-nav a{color:var(--ink);text-decoration:none}
.social{display:flex;gap:16px}
.social span{width:40px;height:40px;display:block}
.social .s1{background:var(--social-a)}
.social .s2{background:var(--social-b)}
.site-header .social{position:absolute;left:1052px;top:56px}
.hero{position:absolute;top:148px;left:0;width:1200px;height:272px;background:linear-gradient(180deg,#1e3566 0%,#2f5aa0 45%,#5a83c4 62%,#1c2c4c 80%,#0e1626 100%)}
.section-title{font-weight:400;text-align:center;font-size:34px}
.btn{display:inline-block;background:var(--navy);color:var(--white);font-size:15px;padding:9px 22px;text-decoration:none}
.team{position:absolute;top:440px;left:0;width:1200px;text-align:center}
.team .section-title{margin-bottom:14px}
.team .rule{width:1104px;margin:0 auto 20px;border-top:1px solid var(--rule)}
.team p{width:1104px;margin:0 auto;text-align:left;font-size:15.5px;line-height:24px;color:var(--muted)}
.team .btn{margin-top:40px}
.services{position:absolute;top:900px;left:0;width:1200px;height:500px;background:var(--band);color:var(--white)}
.services .section-title{margin-top:22px}
.services .rule{width:1104px;margin:16px auto 0;border-top:1px solid #666}
.service-cols{position:absolute;top:120px;left:100px;display:flex}
.service-cols ul{list-style:none;font-size:16px}
.service-cols li{height:44px;padding-left:22px;position:relative}
.service-cols li::before{content:"";position:absolute;left:0;top:8px;width:7px;height:7px;border-radius:50%;background:var(--white)}
.service-cols ul:nth-child(1){width:420px}
.service-cols ul:nth-child(2){width:300px}
.services .btn{position:absolute;top:408px;left:50%;transform:translateX(-50%)}
.news{position:absolute;top:1436px;left:0;width:1200px}
.news .rule{width:1104px;margin:16px auto 0;border-top:1px solid var(--rule)}
.news-item{position:absolute;left:72px;width:1080px}
.news-item .photo{position:absolute;left:0;top:0;width:176px;height:188px;background:linear-gradient(135deg,#c99a7a,#7a5a48 55%,#d8cfc4)}
.news-item .body{position:absolute;left:200px;top:8px;width:880px}
.news-item time{font-size:16px;display:block;margin-bottom:14px}
.news-item p{font-style:italic;font-size:15px;line-height:22px;color:var(--muted)}
.news-item .btn{margin-top:26px}
.news-one{top:76px}
.news-two{top:356px}
.news .divider{position:absolute;top:320px;left:48px;width:1104px;border-top:1px solid var(--rule)}
.contact{position:absolute;top:2080px;left:0;width:1200px;height:272px;background:var(--band-dark);color:var(--white)}
.contact .section-title{margin-top:24px;font-size:32px}
.contact .rule{width:1104px;margin:14px auto 0;border-top:1px solid #666}
.contact-address{position:absolute;left:72px;top:104px;font-size:13px;line-height:19px}
.contact-phone{position:absolute;left:432px;top:104px;text-align:center;width:300px}
.contact-phone small{font-size:15px}
.contact-phone strong{display:block;font-weight:400;font-size:38px;margin-top:4px}
.contact-email{position:absolute;left:812px;top:104px;font-size:13px}
.contact-email .social{margin-top:14px}
.contact-email .social span{width:36px;height:36px}
.legal{position:absolute;top:222px;width:1200px;text-align:center;font-size:11px}
.copyright{position:absolute;top:248px;width:1200px;text-align:center;font-size:10px;color:#aaa}
</style>
</head>
<body>
<header class="site-header">
  <div class="brand"><span class="brand-mark"></span><span class="brand-name">Brackwell Counsel Partners</span></div>
  <nav class="main-nav"><a href="#">Home</a><a href="#">About us</a><a href="#">Join us</a><a href="#">Contact</a><a href="#">Blog</a></nav>
  <div class="social"><span class="s1"></span><span class="s2"></span></div>
</header>

<div class="hero" role="img" aria-label="City skyline of illuminated towers at night over a waterfront"></div>

<section class="team">
  <h2 class="section-title">Our Team</h2>
  <div class="rule"></div>
  <p>We are Immigration Lawyers regulated by the Migration Advice Standards Board (MASB) at the highest level (Level 3) and accredited by The Solicitors Practice Council in England and Wales. We are a member of IPF (Immigration Practitioners Forum) and the MWA (Migrant Welfare Alliance). We pride ourselves by being able to handle complex and sensitive cases. This also means that our clients can deal with us with full confidence when they engage us for their immigration matters. We believe that Immigration Lawyers should be professionals in all dealings and we are passionate about this to be able to assist you as good as we can.</p>
  <a class="btn" href="#">Read more</a>
</section>

<section class="services">
  <h2 class="section-title">Services</h2>
  <div class="rule"></div>
  <div class="service-cols">
    <ul><li>Entry Clearance /Dependent Visas</li><li>Immigration Appeals</li><li>Settlement Applications /ILR</li></ul>
    <ul><li>Domestic Workers Visa</li><li>Student Visa</li><li>Overstayers</li></ul>
    <ul><li>Deportations</li><li>Immigration Detentions</li></ul>
  </div>
  <a class="btn" href="#">Learn more</a>
</section>

<section class="news">
  <h2 class="section-title">News &amp; Publications</h2>
  <div class="rule"></div>
  <article class="news-item news-one">
    <div class="photo" role="img" aria-label="Portrait photo of a couple"></div>
    <div class="body">
      <time>7 December 2014</time>
      <p>We handled a case where a Filipina was in a relationship with an EU national. It was just as difficult because the Filipina was an overstayer. The first application was refused from other solicitor and they came over to see us in our London Office. There was a mistake on the application lodged and we challenged the legality of the refusal on the points of law. We represented her legally in Court and the appeal was allowed. The visa was then granted.</p>
      <a class="btn" href="#">Read more</a>
    </div>
  </article>
  <div class="divider"></div>
  <article class="news-item news-two">
    <div class="photo" role="img" aria-label="Photo of a mother with her child"></div>
    <div class="body">
      <time>8 June 2014</time>
      <p>An overstayer Filipina was encountered and arrested by the Immigration Police. She was eventually detained at Harrowfield Removal Centre in Northamptonshire. We made an application for bail and was granted to be released. We then applied for her family life in the UK as the mother of a child. The visa application was granted. Happy days!</p>
      <a class="btn" href="#">Read more</a>
    </div>
  </article>
</section>

<footer class="contact">
  <h2 class="section-title">Contact Us</h2>
  <div class="rule"></div>
  <address class="contact-address" style="font-style:normal">London Office<br>Brackwell Counsel Partners<br>48 Harrowby Lane<br>London W2 4QT</address>
  <div class="contact-phone"><small>For an immediate consultation</small><strong>0207 555 0148</strong></div>
  <div class="contact-email">Email: info@brackwellcounsel.co.uk
    <div class="social"><span class="s1"></span><span class="s2"></span></div>
  </div>
  <p class="legal">Regulated by the Migration Advice Standards Board and accredited by the Solicitors Practice Council in England and Wales</p>
  <p class="copyright">© 2015 by Brackwell Counsel Partners</p>
</footer>
</body>
</html>
```